Insurance company needs a business card design

We need a business card design for a Massachusetts-based insurance company Veloria Insurance, LLC. We provide auto insurance to Hispanic (Spanish- or Portuguese-speaking) immigrants in the United States. We will give these business cards to auto dealers where such customers typically go to purchase vehicles. We will provide a solution to the dealers to provide easy insurance to the customers buying cars at their dealerships. Veloria is the Spanish word for protection.
Contact Information for Business Card
Name, Designation, Company Name, Address, Phone Number, Email, Website
Look and feel
Each slider illustrates characteristics of the customer's brand and the style your logo design should communicate.

```html
<!DOCTYPE html>
<html lang="en">
<head>
<meta charset="utf-8">
<title>Veloria Insurance – Business Card</title>
<link href="https://fonts.googleapis.com/css2?family=Montserrat:wght@400;500;700;800&display=swap" rel="stylesheet">
<style>
  :root {
    --navy: #024b7c;
    --navy-deep: #013f69;
    --orange: #f18400;
    --white: #ffffff;
    --ink: #111111;
    --stage: #efefef;
    --wave-light: #eef0f7;
  }
  * { box-sizing: border-box; margin: 0; padding: 0; }
  html, body { width: 1200px; height: 1200px; overflow: hidden; }
  body {
    background: var(--stage);
    font-family: "Montserrat", sans-serif;
    position: relative;
  }
  .card {
    position: absolute;
    left: 203px;
    width: 794px;
    height: 453px;
    border-radius: 47px;
    overflow: hidden;
  }
  .card-front { top: 102px; }
  .card-back { top: 644px; }

  .pattern { position: absolute; inset: 0; }
  .card-front .pattern { background: linear-gradient(160deg, var(--navy) 0%, var(--navy-deep) 100%); }
  .card-back .pattern { background: linear-gradient(160deg, var(--white) 0%, var(--wave-light) 100%); }

  /* Front */
  .front-brand {
    position: absolute;
    left: 0; right: 0; top: 0; bottom: 0;
    display: flex;
    flex-direction: column;
    align-items: center;
    justify-content: center;
    gap: 28px;
  }
  .front-mark {
    width: 120px; height: 120px;
    border-radius: 50%;
    background: var(--orange);
  }
  .front-name {
    color: var(--white);
    font-weight: 800;
    font-size: 50px;
    letter-spacing: 0.04em;
    text-transform: uppercase;
  }

  /* Back */
  .contact-panel {
    position: absolute;
    left: 0; top: 65px;
    width: 470px; height: 325px;
    background: var(--orange);
    clip-path: polygon(0 0, 375px 0, 470px 162px, 375px 325px, 0 325px);
  }
  .contact-list { list-style: none; }
  .contact-item {
    position: absolute;
    left: 52px;
    display: flex;
    align-items: center;
    gap: 12px;
    color: var(--white);
    font-weight: 700;
    font-size: 15px;
    letter-spacing: 0.28em;
  }
  .contact-icon {
    width: 33px; height: 33px;
    border: 2px solid var(--white);
    border-radius: 50%;
    display: flex; align-items: center; justify-content: center;
    flex-shrink: 0;
  }
  .contact-icon svg { width: 16px; height: 16px; }

  .back-brand {
    position: absolute;
    right: 46px; top: 26px;
    display: flex; align-items: center; gap: 10px;
  }
  .back-mark { width: 40px; height: 40px; border-radius: 50%; background: var(--orange); }
  .back-name {
    color: var(--navy);
    font-weight: 800;
    font-size: 23px;
    letter-spacing: 0.04em;
    text-transform: uppercase;
  }

  .holder {
    position: absolute;
    left: 494px; width: 240px;
    top: 180px;
    text-align: center;
    color: var(--ink);
  }
  .holder-name { font-size: 27px; font-weight: 400; white-space: nowrap; }
  .holder-name strong { font-weight: 700; }
  .holder-rule { width: 197px; height: 2px; background: var(--orange); margin: 9px auto 10px; }
  .holder-position { font-size: 23px; font-weight: 400; letter-spacing: 0.18em; }
</style>
</head>
<body>

<section class="card card-front">
  <div class="pattern" role="img" aria-label="Navy card face with fine wavy line pattern"></div>
  <div class="front-brand">
    <div class="front-mark"></div>
    <div class="front-name">Veloria Insurance</div>
  </div>
</section>

<section class="card card-back">
  <div class="pattern" role="img" aria-label="White card face with light wavy line pattern"></div>

  <div class="contact-panel"></div>
  <ul class="contact-list">
    <li class="contact-item" style="top:141px">
      <span class="contact-icon">
        <svg viewBox="0 0 16 16" fill="none" stroke="#fff" stroke-width="1.8"><path d="M8 15s5-5 5-8.5A5 5 0 0 0 3 6.5C3 10 8 15 8 15z"/><circle cx="8" cy="6.5" r="1.7"/></svg>
      </span>
      123 LOREM,IPSUM
    </li>
    <li class="contact-item" style="top:190px">
      <span class="contact-icon">
        <svg viewBox="0 0 16 16" fill="none" stroke="#fff" stroke-width="1.8" stroke-linejoin="round"><path d="M3 2h3l1.2 3-1.8 1.2a8 8 0 0 0 4.4 4.4L11 8.8l3 1.2v3a1 1 0 0 1-1 1A12 12 0 0 1 2 3a1 1 0 0 1 1-1z"/></svg>
      </span>
      +00-0000-0000-000
    </li>
    <li class="contact-item" style="top:240px">
      <span class="contact-icon">
        <svg viewBox="0 0 16 16" fill="none" stroke="#fff" stroke-width="1.6"><rect x="1.5" y="3.5" width="13" height="9"/><path d="M1.5 3.5 8 9l6.5-5.5M1.5 12.5 6 8M14.5 12.5 10 8"/></svg>
      </span>
      INFO@COMPANYNAME.COM
    </li>
    <li class="contact-item" style="top:291px">
      <span class="contact-icon">
        <svg viewBox="0 0 16 16" fill="#fff"><path d="M4 1.5v12l3-3 2 4.5 2-.9-2-4.4h4.2z"/></svg>
      </span>
      WWW.COMPANYNAME.COM
    </li>
  </ul>

  <div class="back-brand">
    <div class="back-mark"></div>
    <div class="back-name">Veloria Insurance</div>
  </div>

  <div class="holder">
    <p class="holder-name">NAME <strong>SURNAME</strong></p>
    <div class="holder-rule"></div>
    <p class="holder-position">POSITION</p>
  </div>
</section>

</body>
</html>
```